Dental FAQ/advert tri-fold for holistic family dentist

We are a dental clinic with a holistic emphasis. We are seeking new clients, mainly middle classed families. A tri-fold brochure that is both a useful dental FAQ to keep in the house and acts as an advertisement for our clinic. It will be mailed out. It needs to look clean, modern, somewhat minimalist, and I want it to follow the Orble design esthetic. website is willowcrestdentalcare.com
Updates

I just updated the pamphlet file with revised text! Thanks for the nice designs so far, keep em coming.

Target Market(s)

Young families. Upper middle classes.

Industry/Entity Type

Dental

Requirements
Must have
• Follows our logo and colours.

```html
<!DOCTYPE html>
<html lang="en">
<head>
<meta charset="utf-8">
<title>Willowcrest Dental Care – Frequently Asked Questions Brochure</title>
<link rel="stylesheet" href="https://fonts.googleapis.com/css2?family=Arimo:wght@400;700&family=Open+Sans:wght@300;400;600;700&family=Lora:wght@400;700&family=Raleway:wght@700&display=swap">
<style>
  :root {
    --page: #e6e9ec;
    --paper: #ffffff;
    --blue: #1b56c8;
    --blue-deep: #1142a8;
    --green: #34a82c;
    --green-bright: #4cbd22;
    --green-text: #2f9a25;
    --grey-text: #8b9096;
    --ink: #4a4f55;
    --mist: #eceef0;
  }
  * { box-sizing: border-box; margin: 0; padding: 0; }
  html, body { width: 789px; height: 1200px; overflow: hidden; }
  body { background: var(--page); position: relative; font-family: "Open Sans", sans-serif; }

  .sheet { position: absolute; left: 40px; width: 709px; height: 540px; background: var(--paper); overflow: hidden; }
  .sheet--outside { top: 30px; }
  .sheet--inside { top: 630px; }
  .layer { position: absolute; left: 0; top: 0; width: 709px; height: 540px; }
  .abs { position: absolute; }

  /* brand lockup */
  .brand { position: absolute; display: flex; align-items: center; gap: 7px; color: var(--green); font-family: "Open Sans", sans-serif; font-weight: 600; }
  .brand__dot { width: 12px; height: 12px; border-radius: 50%; background: var(--green); flex: none; }
  .brand__name { line-height: 1.05; }
  .brand__name span { display: block; }

  /* outside */
  .cover-title { left: 30px; top: 14px; width: 210px; font-family: "Arimo", sans-serif; font-weight: 700; font-size: 17px; line-height: 1.05; color: var(--blue); }
  .cover-copy { left: 30px; top: 56px; width: 208px; font-size: 9.4px; line-height: 1.38; color: var(--grey-text); }
  .tooth-art { left: 42px; top: 224px; width: 58px; height: 52px; border-radius: 45%; background: radial-gradient(circle at 40% 35%, #ffffff, #d8dde2); }
  .faq-card { left: 30px; top: 266px; width: 216px; height: 280px; background: var(--blue); border-radius: 16px 16px 0 0; padding: 7px 7px 0; color: #fff; }
  .faq-card__pill { background: #fff; color: var(--blue); border-radius: 10px; font-family: "Arimo", sans-serif; padding: 3px 8px; }
  .faq-card__pill--small { font-size: 9.2px; }
  .faq-card__pill--large { font-size: 13.5px; padding: 2px 8px; margin-top: 6px; }
  .faq-card p { font-size: 9.2px; line-height: 1.35; padding: 4px 6px 0; }
  .knock-label { left: 250px; top: 14px; background: var(--green-bright); color: #fff; font-family: "Arimo", sans-serif; font-weight: 700; font-size: 8px; padding: 2px 8px; border-radius: 9px; }
  .knock-copy { left: 252px; top: 32px; width: 205px; font-family: "Raleway", sans-serif; font-weight: 700; font-size: 7.4px; line-height: 1.95; color: var(--blue); text-transform: uppercase; }
  .guard-box { left: 250px; top: 168px; width: 200px; height: 124px; border-radius: 14px; background: linear-gradient(#f4f5f6, #d9dcdf); padding: 10px 10px; text-align: center; }
  .guard-box h3 { font-family: "Arimo", sans-serif; font-size: 8.6px; font-weight: 400; color: var(--green-text); line-height: 1.35; margin-bottom: 6px; }
  .guard-box p { font-family: "Arimo", sans-serif; font-size: 8.5px; font-weight: 700; color: var(--blue); line-height: 1.35; }
  .whiten { left: 248px; top: 444px; width: 216px; text-align: center; font-family: "Arimo", sans-serif; font-size: 8.4px; line-height: 1.3; }
  .whiten h3 { font-weight: 400; color: var(--blue); font-size: 8.4px; }
  .whiten p { color: #fff; font-weight: 700; }
  .doctor-photo { left: 478px; top: 158px; width: 196px; height: 290px; background: linear-gradient(180deg, #e8ebee 0%, #f7f8f9 45%, #dfe3e7 100%); }
  .cover-tagline { left: 470px; top: 452px; width: 222px; text-align: right; color: #fff; font-weight: 300; font-size: 15px; line-height: 1.22; }

  /* inside */
  .col-left { left: 22px; top: 44px; width: 196px; font-family: "Lora", serif; }
  .col-left h3, .col-mid h3 { font-size: 7.6px; font-weight: 700; color: var(--green-text); line-height: 1.3; }
  .col-left p { font-size: 7.4px; line-height: 1.42; color: var(--ink); margin-bottom: 9px; }
  .col-left p:first-of-type { color: var(--grey-text); }
  .soft-panel { left: 12px; top: 36px; width: 208px; height: 494px; border-radius: 16px; background: rgba(205, 210, 215, 0.38); }
  .col-mid { font-family: "Lora", serif; font-size: 7.4px; line-height: 1.4; }
  .col-mid p { color: #fff; }
  .white-box { background: #fff; border: 2px solid #c9ccd0; border-radius: 12px; padding: 6px 7px; }
  .white-box p { color: var(--blue); }
  .white-box h3.big { font-size: 10px; color: var(--blue-deep); }
  .col-right { left: 466px; top: 86px; width: 228px; font-family: "Lora", serif; }
  .col-right h3 { font-size: 8.3px; font-weight: 700; color: var(--blue); line-height: 1.3; }
  .col-right p { font-size: 8px; line-height: 1.38; color: var(--grey-text); margin-bottom: 12px; }
</style>
</head>
<body>

<!-- Outside spread -->
<section class="sheet sheet--outside">
  <svg class="layer" viewBox="0 0 709 540" aria-hidden="true">
    <defs>
      <linearGradient id="mistFade" x1="0" y1="0" x2="0" y2="1">
        <stop offset="0" stop-color="#ffffff"/><stop offset="1" stop-color="#eef0f2"/>
      </linearGradient>
      <linearGradient id="blueBand" x1="0" y1="1" x2="1" y2="0">
        <stop offset="0" stop-color="#1142a8"/><stop offset="1" stop-color="#2a6ae0"/>
      </linearGradient>
    </defs>
    <rect width="709" height="540" fill="url(#mistFade)"/>
    <path d="M240 540 L240 300 C 300 280 360 250 410 200 C 480 120 580 50 709 20 L709 48 C 600 80 510 150 450 230 C 400 290 330 320 240 340 Z" fill="url(#blueBand)"/>
    <path d="M450 235 C 520 150 610 95 709 70 L709 78 C 615 104 530 160 462 238 Z" fill="#c9ced3"/>
  </svg>

  <div class="abs doctor-photo" role="img" aria-label="Portrait photo of a smiling dentist in a white coat with a stethoscope"></div>

  <svg class="layer" viewBox="0 0 709 540" aria-hidden="true">
    <defs>
      <linearGradient id="greenBase" x1="0" y1="0" x2="0" y2="1">
        <stop offset="0" stop-color="#4cbd22"/><stop offset="1" stop-color="#2a9a22"/>
      </linearGradient>
    </defs>
    <path d="M240 540 L240 420 C 360 430 520 430 709 360 L709 540 Z" fill="url(#greenBase)"/>
    <path d="M330 432 C 470 440 600 420 709 372 L709 382 C 600 432 470 452 330 440 Z" fill="#b8bec4"/>
    <path d="M380 425 C 500 428 610 400 709 350 L709 358 C 610 410 500 436 380 431 Z" fill="#ffffff"/>
  </svg>

  <h2 class="abs cover-title">How can I manage my sensitive teeth?</h2>
  <p class="abs cover-copy">While using a soft bristled toothbrush as well as desensitizing toothpaste are frequently helpful, many people still experience painful teeth sensitivity which can interfere with the enjoyment of many foods. We are pleased to offer effective laser desensitization of teeth which is both gentle and painless. Other dental procedures that may help reduce sensitivity including use of white fillings or dentin sealers to cover exposed root surfaces, or use of a mouth guard to prevent further enamel erosion.</p>
  <div class="abs tooth-art" role="img" aria-label="Cartoon tooth holding a toothbrush"></div>

  <div class="abs faq-card">
    <div class="faq-card__pill faq-card__pill--small">Do I need to have my wisdom teeth removed?</div>
    <p>While some people keep their wisdom teeth well into adulthood, wisdom teeth often don't grow in properly and need to be removed before they become a problem. This usually happens between the ages of 16-22. Everybody is different and your dental provider will assess your teeth.</p>
    <div class="faq-card__pill faq-card__pill--large">What can cause a toothache?</div>
    <p>Toothaches are either caused by an irritated nerve within the tooth, or an infection surrounding the tooth. Usually over the counter pain medication like Ibuprofen can be used for temporary relief before your appointment. At your visit, our dentist will determine the exact cause of the problem and provide treatment options.</p>
  </div>

  <div class="abs knock-label">WHAT SHOULD I DO IF I KNOCK A TOOTH OUT?</div>
  <p class="abs knock-copy">Say sorry to the other person! Just kidding, if a tooth is knocked clear out, it can sometimes be re-implanted, if done within 30-60 minutes. Gently rinse the tooth off, and store it in a solution of milk or clean water and make your way to a dentist asap.</p>

  <div class="abs guard-box">
    <h3>Should I wear a mouth guard during recreational activities?</h3>
    <p>Mouth guards should be used by anyone who plays contact sports such as hockey, football, boxing, soccer, basketball, and lacrosse. Your dentist can create a custom appliance that provides much more comfort and protection than a store-bought appliance.</p>
  </div>

  <div class="brand" style="left:292px; top:348px; font-size:11px;">
    <span class="brand__dot"></span>
    <span class="brand__name"><span>Willowcrest</span><span>Dental Care</span></span>
  </div>

  <div class="abs whiten">
    <h3>What's the difference between teeth whitening in a dental office and store bought kits?</h3>
    <p>A dental clinic can supply you with a custom fit tray to maximize your teeth whitening, as well as prescribe stronger formulations of the whitening solution for a longer lasting, whiter smile.</p>
  </div>

  <div class="brand" style="left:500px; top:104px; font-size:17px;">
    <span class="brand__dot" style="width:16px;height:16px;"></span>
    <span class="brand__name"><span>Willowcrest</span><span>Dental Care</span></span>
  </div>

  <p class="abs cover-tagline">Frequently<br>Asked Questions<br>For Your Dentist</p>
</section>

<!-- Inside spread -->
<section class="sheet sheet--inside">
  <svg class="layer" viewBox="0 0 709 540" aria-hidden="true">
    <defs>
      <linearGradient id="midBlue" x1="0" y1="0" x2="0" y2="1">
        <stop offset="0" stop-color="#1f5ed2"/><stop offset="1" stop-color="#1446b0"/>
      </linearGradient>
      <linearGradient id="greenFoot" x1="0" y1="0" x2="0" y2="1">
        <stop offset="0" stop-color="#4cbd22"/><stop offset="1" stop-color="#2a9a22"/>
      </linearGradient>
    </defs>
    <rect x="233" y="0" width="220" height="540" fill="url(#midBlue)"/>
    <path d="M0 40 C 120 22 260 10 453 14 L453 0 L0 0 Z" fill="#ffffff"/>
    <path d="M0 46 C 120 26 260 14 453 18 L453 8 C 260 4 120 14 0 30 Z" fill="#4cbd22"/>
    <path d="M453 0 L709 0 L709 40 C 640 50 560 58 453 60 Z" fill="#ffffff"/>
    <path d="M453 40 C 560 42 640 30 709 14 L709 34 C 640 48 560 58 453 60 Z" fill="#1b56c8"/>
    <path d="M453 26 C 560 30 640 16 709 4 L709 12 C 640 26 560 38 453 36 Z" fill="#4cbd22"/>
    <path d="M0 505 C 200 525 420 520 709 452 L709 540 L0 540 Z" fill="url(#greenFoot)"/>
    <path d="M453 500 C 560 494 640 476 709 450 L709 462 C 640 490 560 506 453 510 Z" fill="#ffffff"/>
    <path d="M453 486 C 560 482 640 464 709 436 L709 446 C 640 474 560 492 453 496 Z" fill="#b8bec4"/>
  </svg>

  <div class="abs soft-panel"></div>
  <div class="abs col-left">
    <h3>When should my child first start seeing the dentist?</h3>
    <p>The Northern Dental Association recommends bringing your kids to see the dentist 6 months after their first tooth has appeared. We recommend bringing kids in for short "happy visits" that build their confidence and comfort in being at our dental clinic. A happy visit is free unless dental services are provided. Kids can watch you at your appointment and they can learn the fun parts of the dental visit which may include; counting their teeth, polishing their teeth, and riding the dental chair up and down. And of course, the best part, the prize drawer at the end of the appointment! We find that kids who come for happy visits experience little to no dental fear or anxiety in the coming years.</p>
    <h3>How often should I get dental checkups and cleanings?</h3>
    <p>Everybody is different, and has different needs when it comes to regular examinations and cleanings. Most people need to have their teeth cleaned at least every 6 months, and some people may require more if gum disease is present.</p>
    <h3>How do I know my dental office is clean?</h3>
    <p>Dental offices in our province follow the most stringent regulations in the world for sterilization and infection control. The operatory's are cleaned between every patient, staff members thoroughly wash their hands regularly, and items are put through an auto-clave system for sterilization. When in doubt, ask, and dental staff members should be happy to show you exactly how your safety is protected.</p>
    <h3>Can I see the dentist if I am pregnant?</h3>
    <p>Regular dental cleanings are vitally important during pregnancy, as pregnancy gingivitis affects up to 30-70% of pregnant women and gum disease has been linked to low birth weight and premature delivery. We recommend</p>
  </div>

  <div class="abs col-mid" style="left:243px; top:26px; width:202px;">
    <p>a thorough dental exam and cleaning if you are pregnant or planning on having a baby.</p>
  </div>
  <div class="abs col-mid white-box" style="left:240px; top:74px; width:208px; height:136px;">
    <h3>What are some of the latest technologies available for improving my oral health?</h3>
    <p>Dentistry is always improving and your treatment and safety can be augmented with new technologies. For example, digital x-rays can greatly reduce your exposure to radiation. Lasers are a non-invasive way to quickly and easily kill bacteria in your gums. Speed braces can straighten your teeth much faster than traditional braces.</p>
  </div>
  <div class="abs col-mid" style="left:243px; top:216px; width:202px;">
    <h3>How can I get my records transferred to a new dental office?</h3>
    <p>It's as simple as asking your former dental office to send the records to the new office. Sometimes you may be requested to sign a release and consent form too. We are happy to help you with the process.</p>
  </div>
  <div class="abs col-mid white-box" style="left:240px; top:300px; width:208px; height:146px;">
    <h3 class="big">Is fluoride safe?</h3>
    <p>The National Oral Health Survey 2007-2009 found that 16% of children have mild forms of dental fluorosis that often go unnoticed. Dental fluorosis is a change in the appearance of teeth, often causing small white specks to appear. It is caused when higher than optimal amounts of fluoride are ingested in early childhood. Fluoride-free options for dental care are available.</p>
  </div>
  <div class="abs col-mid" style="left:243px; top:452px; width:202px;">
    <h3>Are amalgam fillings containing mercury safe?</h3>
    <p>The National Health Agency's official position is that amalgams are safe, but should be avoided in certain people with medical conditions. It is best to consult with your dentist directly. Mercury-free options for dental care are available, and we offer a specific method of mercury removal too.</p>
  </div>

  <div class="abs col-right">
    <h3>What are dental sealants, and do they contain BPA?</h3>
    <p>Dental sealants are a way to protect a tooth from forming a cavity by sealing the natural pits and grooves in a tooth with resin. Some sealants don't contain Bis-phenol A, and you may ask your dentist if the type he or she uses has BPA.</p>
    <h3>What is gum disease and how can it affect my health?</h3>
    <p>Gum disease, or periodontal disease, is when bacteria and tartar on your teeth cause inflammation of the gums and the bone holding teeth in. When severe enough, bone loss occurs, leading to loose teeth and gum abscesses. Gum disease can be treated by daily flossing and regular dental cleaning appointments. Your dentist and dental hygienist are able to discuss treatment options available for you.</p>
    <h3>What do I do about bad breath?</h3>
    <p>80% of bad breath comes from an oral source. For instance, cavities or gum disease can lead to bad breath, as can cracked fillings, and less-than-clean dentures. An examination by a dentist to discover the source of the problem, as well as a strong oral hygiene regimen, will frequently alleviate this embarrassing problem.</p>
  </div>

  <div class="brand" style="left:508px; top:430px; font-size:15px;">
    <span class="brand__dot" style="width:14px;height:14px;"></span>
    <span class="brand__name"><span>Willowcrest</span><span>Dental Care</span></span>
  </div>
</section>

</body>
</html>
```